Letterhead Design Project

Looking for letterhead designs for Brastova Mining.

I am looking for a letterhead design in conjunction with a business card design. I have opened contests for both but ask that if you submit a letterhead design you also submit a business card design with a corresponding look/feel.

Brastova Mining is a B2B company that buys and sells large machinery tires within the coal mining industry. The design should the strong, crisp and masculine. I have uploaded the company logo and mock-up of the back of the company's business card.

Color scheme should be grey/green/black

Contact information to include:
Name: Dale Whitford
Title: Managing Director
Phone: 555-231-4097
Address: 1817 Pellam #3 Dallas, TX 75290
Email: Dale@Brastova.example
Updates

Project Deadline Extended
Reason: Looking for a more refined, elegant letterhead than what's been submitted as of yet. Here is a sample of what we're looking for: http://www.plumcrestgallery.example/letterhead-designs/ We will also be increasing the payment.

Industry/Entity Type

Coal Mining

```html
<!DOCTYPE html>
<html lang="en">
<head>
<meta charset="utf-8">
<title>Brastova Mining – Letterhead &amp; Business Card</title>
<link rel="stylesheet" href="https://fonts.googleapis.com/css2?family=Arimo:wght@400;700&display=swap">
<style>
  :root {
    --backdrop: #3b3b3d;
    --charcoal: #1f1f20;
    --charcoal-edge: #262627;
    --paper: #ffffff;
    --ink-light: #ffffff;
    --ink-soft: #e6e6e6;
    --green: #5cb144;
    --rule: #d9d9d9;
  }
  * { margin: 0; padding: 0; box-sizing: border-box; }
  html, body { width: 1200px; height: 900px; overflow: hidden; }
  body {
    position: relative;
    background: var(--backdrop);
    font-family: "Arimo", Arial, sans-serif;
    color: var(--ink-light);
  }

  /* Letterhead */
  .letterhead {
    position: absolute; left: 42px; top: 33px;
    width: 588px; height: 835px;
    background: var(--paper);
    box-shadow: 0 4px 14px rgba(0,0,0,.45);
  }
  .letterhead-header {
    position: absolute; left: 0; top: 0; width: 100%; height: 97px;
    background: linear-gradient(180deg, var(--charcoal-edge), var(--charcoal));
  }
  .letterhead-footer {
    position: absolute; left: 0; bottom: 0; width: 100%; height: 116px;
    background: linear-gradient(180deg, var(--charcoal-edge), var(--charcoal));
  }

  /* Brand name stand-in */
  .brand {
    position: absolute; display: flex; align-items: center; gap: 10px;
    font-weight: 700; color: var(--ink-light);
    letter-spacing: .04em; white-space: nowrap; text-transform: uppercase;
  }
  .brand-mark { display: block; background: var(--green); }

  .letterhead-header .brand { left: 34px; top: 30px; font-size: 26px; }
  .letterhead-header .brand-mark { width: 16px; height: 16px; }

  .letterhead-footer .brand { left: 78px; top: 16px; font-size: 30px; }
  .letterhead-footer .brand-mark { width: 16px; height: 16px; }
  .letterhead-footer .rule {
    position: absolute; left: 19px; top: 65px; width: 347px;
    border-top: 1px solid var(--rule);
  }
  .contact {
    position: absolute; display: flex; align-items: center; gap: 5px;
    color: var(--ink-light); white-space: nowrap;
  }
  .contact svg { fill: currentColor; flex: none; }
  .letterhead-footer .contact { font-size: 10.5px; top: 89px; }
  .letterhead-footer .contact.phone { left: 19px; }
  .letterhead-footer .contact.address { left: 201px; }

  /* Business cards */
  .card {
    position: absolute; left: 650px; width: 518px; height: 307px;
    background: linear-gradient(160deg, #2a2a2b, var(--charcoal));
    box-shadow: 0 4px 14px rgba(0,0,0,.45);
  }
  .card-front { top: 101px; }
  .card-back { top: 503px; }

  .card-front .brand { left: 28px; top: 33px; font-size: 34px; }
  .card-front .brand-mark { width: 20px; height: 20px; }
  .holder-name {
    position: absolute; left: 26px; top: 180px;
    font-size: 19px; font-weight: 400; color: var(--ink-soft);
  }
  .holder-title {
    position: absolute; left: 26px; top: 203px;
    font-size: 13.5px; color: var(--ink-soft);
  }
  .card-front .rule {
    position: absolute; left: 26px; top: 231px; width: 480px;
    border-top: 1px solid var(--rule);
  }
  .card-front .contact { font-size: 13.5px; }
  .card-front .contact.phone { left: 27px; top: 246px; }
  .card-front .contact.email { left: 27px; top: 265px; }
  .card-front .contact.address { left: 280px; top: 265px; }

  .card-back .brand { right: 24px; bottom: 32px; font-size: 34px; }
  .card-back .brand-mark { width: 20px; height: 20px; }
</style>
</head>
<body>

  <section class="letterhead" aria-label="Letterhead">
    <header class="letterhead-header">
      <div class="brand"><span class="brand-mark"></span>Brastova Mining</div>
    </header>
    <footer class="letterhead-footer">
      <div class="brand"><span class="brand-mark"></span>Brastova Mining</div>
      <div class="rule"></div>
      <div class="contact phone">
        <svg width="11" height="11" viewBox="0 0 24 24"><path d="M6.6 10.8a15.1 15.1 0 0 0 6.6 6.6l2.2-2.2a1 1 0 0 1 1-.25 11.4 11.4 0 0 0 3.6.57 1 1 0 0 1 1 1V20a1 1 0 0 1-1 1A17 17 0 0 1 3 4a1 1 0 0 1 1-1h3.5a1 1 0 0 1 1 1c0 1.25.2 2.45.57 3.57a1 1 0 0 1-.25 1z"/></svg>
        555-231-4097
      </div>
      <div class="contact address">
        <svg width="9" height="12" viewBox="0 0 18 24"><path d="M9 0a9 9 0 0 0-9 9c0 6.75 9 15 9 15s9-8.25 9-15a9 9 0 0 0-9-9zm0 12.5A3.5 3.5 0 1 1 9 5.5a3.5 3.5 0 0 1 0 7z"/></svg>
        1817 Pellam #3 Dallas, TX 75290
      </div>
    </footer>
  </section>

  <section class="card card-front" aria-label="Business card front">
    <div class="brand"><span class="brand-mark"></span>Brastova Mining</div>
    <div class="holder-name">Dale Whitford</div>
    <div class="holder-title">Managing Director</div>
    <div class="rule"></div>
    <div class="contact phone">
      <svg width="15" height="15" viewBox="0 0 24 24"><path d="M6.6 10.8a15.1 15.1 0 0 0 6.6 6.6l2.2-2.2a1 1 0 0 1 1-.25 11.4 11.4 0 0 0 3.6.57 1 1 0 0 1 1 1V20a1 1 0 0 1-1 1A17 17 0 0 1 3 4a1 1 0 0 1 1-1h3.5a1 1 0 0 1 1 1c0 1.25.2 2.45.57 3.57a1 1 0 0 1-.25 1z"/></svg>
      555-231-4097
    </div>
    <div class="contact email">
      <svg width="15" height="11" viewBox="0 0 24 17"><path d="M0 0h24v17H0zM2 2v.6l10 7 10-7V2zm0 3v10h20V5l-10 7z"/></svg>
      Dale@Brastova.example
    </div>
    <div class="contact address">
      <svg width="11" height="14" viewBox="0 0 18 24"><path d="M9 0a9 9 0 0 0-9 9c0 6.75 9 15 9 15s9-8.25 9-15a9 9 0 0 0-9-9zm0 12.5A3.5 3.5 0 1 1 9 5.5a3.5 3.5 0 0 1 0 7z"/></svg>
      1817 Pellam #3 Dallas, TX 75290
    </div>
  </section>

  <section class="card card-back" aria-label="Business card back">
    <div class="brand"><span class="brand-mark"></span>Brastova Mining</div>
  </section>

</body>
</html>
```